Redesign a programmers open source website

This is a fairly old website (started 1999) that hosts lots of programming-related stuff, from the useful (freeware tools, articles on programming topics) to the obscure (esoteric programming languages, tips on code obfuscation and bad examples), plus a couple of other bits thrown in. It is 100% open source and free. However, it looks a bit boring, so I want to liven up the design, and make it the basis for a future portfolio showcase. The design should be compatible with bootstrap (i.e. work on mobile devices).

Take a look at the existing one over at
http://q-vorx-z.net

Requirements
Must have
• After reviewing the designs submitted so far:
• - something reduced and elegant
• - something that is not too noisy, but instead reflects quality.
• - I would like to see two pages: the frontpage, and one text-heavy (for example, an article on one of my programming languages).

```html
<!DOCTYPE html>
<html lang="en">
<head>
<meta charset="utf-8">
<title>q-vorx-z.net</title>
<link href="https://fonts.googleapis.com/css2?family=Open+Sans:ital,wght@0,400;0,600;0,700;1,400&display=swap" rel="stylesheet">
<style>
:root{
  --blue:#1f6fb0;
  --orange:#f07a1e;
  --ink:#333;
  --rule:#e2e2e2;
  --grey-band:#ebebeb;
  --footer:#2f3538;
  --footer-bottom:#262b2d;
  --footer-text:#9aa3a7;
  --quote-text:#c8cdd0;
}
*{margin:0;padding:0;box-sizing:border-box}
html,body{width:865px;height:1200px;overflow:hidden;background:#fff}
body{font-family:"Open Sans",Arial,sans-serif;color:var(--ink)}
.page{position:relative;width:865px;height:1200px}
.abs{position:absolute}

.site-header{position:absolute;left:0;top:0;width:865px;height:56px;border-bottom:1px solid var(--rule)}
.brand{left:72px;top:8px;display:flex;align-items:center;gap:8px}
.brand-dot{width:40px;height:40px;border-radius:50%;background:var(--blue)}
.brand-name{font-size:18px;font-weight:700;color:#7a7a7a}
.search{left:530px;top:19px;width:22px;height:22px;border-radius:50%;border:1px solid #ddd;background:#f4f4f4}
.connect{left:569px;top:25px;font-size:8px;color:#555}
.social{top:20px;width:20px;height:20px;border-radius:50%;background:var(--blue)}

.main-nav{position:absolute;left:0;top:56px;width:865px;height:35px;background:linear-gradient(#fff,#f3f3f3);border-bottom:1px solid #d8d8d8}
.nav-item{position:absolute;top:12px;font-size:9.5px;color:#555;transform:translateX(-50%)}
.nav-item.active{color:#333}
.nav-underline{left:78px;top:32px;width:60px;height:3px;background:var(--blue)}

.hero{position:absolute;left:0;top:91px;width:865px;height:325px;background:linear-gradient(100deg,#f4efea 0%,#e8ddd3 40%,#b99a80 70%,#8a6a54 100%)}
.hero-title{left:73px;top:72px;font-size:25px;line-height:31px;font-weight:700;color:var(--blue)}
.hero-sub{left:73px;top:142px;font-size:14px;line-height:22px;color:#222}
.hero-btn{left:74px;top:199px;width:122px;height:30px;background:var(--orange);color:#fff;font-size:9.5px;display:flex;align-items:center;justify-content:center}

.welcome-title{left:0;top:463px;width:865px;text-align:center;font-size:16px;font-weight:700;color:var(--blue)}
.welcome-text{left:120px;top:497px;width:625px;text-align:center;font-size:8.6px;line-height:18.5px;color:#555}

.feature-icon{top:576px;width:40px;height:40px;background:var(--blue);display:flex;align-items:center;justify-content:center}
.feature-title{top:577px;font-size:9.5px;color:#333;font-weight:600}
.feature-text{top:596px;font-size:8px;line-height:16px;color:#555;width:170px}

.news{position:absolute;left:0;top:670px;width:865px;height:303px;background:var(--grey-band)}
.news-title{left:71px;top:34px;font-size:12px;font-weight:700;color:var(--blue)}
.news-intro{left:71px;top:56px;font-size:8.6px;color:#555}
.news-photo{top:93px;width:166px;height:112px}
.news-caption{top:216px;width:170px;font-size:9.2px;line-height:16px;font-weight:600;color:#333}
.news-date{top:252px;font-size:9.2px;color:#555}

.site-footer{position:absolute;left:0;top:973px;width:865px;height:192px;background:var(--footer)}
.footer-head{top:33px;font-size:11px;color:#fff;font-weight:400}
.footer-arrows{left:511px;top:33px;font-size:9px;color:#aaa;letter-spacing:4px}
.quote{top:63px;width:182px;font-family:Arial,Helvetica,sans-serif;font-size:7.3px;line-height:14.8px;font-style:italic;color:var(--quote-text)}
.quote-mark{font-size:18px;line-height:18px;color:#9aa3a7;font-family:Georgia,serif}
.quote-author{top:150px;font-size:7.6px;color:#7d868a}
.quote-author b{color:var(--quote-text)}
.footer-links{top:55px;font-size:8px;line-height:16px;color:var(--footer-text);list-style:none}
.copyright{position:absolute;left:0;top:1165px;width:865px;height:35px;background:var(--footer-bottom);color:#9aa3a7;font-size:8px;text-align:center;line-height:35px}
</style>
</head>
<body>
<div class="page">
  <header class="site-header">
    <div class="abs brand"><span class="brand-dot"></span><span class="brand-name">q-vorx-z.net</span></div>
    <div class="abs search"></div>
    <div class="abs connect">Connect with our social network :</div>
    <span class="abs social" style="left:700px;background:#2a5ea8"></span>
    <span class="abs social" style="left:724px;background:#3ba2e0"></span>
    <span class="abs social" style="left:748px;background:#f0a01e"></span>
    <span class="abs social" style="left:773px;background:#1f6f8f"></span>
  </header>

  <nav class="main-nav">
    <span class="nav-item active" style="left:110px">Home</span>
    <span class="nav-item" style="left:212px">Programming</span>
    <span class="nav-item" style="left:325px">Languages</span>
    <span class="nav-item" style="left:434px">Obfuscation</span>
    <span class="nav-item" style="left:544px">Downloads</span>
    <span class="nav-item" style="left:646px">Interests</span>
    <span class="nav-item" style="left:749px">Contact us</span>
    <span class="abs nav-underline"></span>
  </nav>

  <section class="hero" role="img" aria-label="Photo of a hand typing on a white computer keyboard">
    <h1 class="abs hero-title">A BEWILDERING<br>ASSORTMENT OF FALSE</h1>
    <p class="abs hero-sub">WELCOME TO MY WEBSITE, FRESHLY REDESIGNED<br>FOR READING ON MOBILE DEVICES.</p>
    <a class="abs hero-btn">VIEW MORE INFO</a>
  </section>

  <h2 class="abs welcome-title">WELCOME TO Q-VORX-Z</h2>
  <p class="abs welcome-text">Welcome to my website, freshly redesigned for reading on mobile devices. I am still working on refreshing many of the old pages - for example, porting Serpentix 2.3 code from way pack to more current revisions; updating page styles and so on. Bear with me, this is work in progress...</p>

  <div class="abs feature-icon" style="left:71px"><svg width="22" height="18" viewBox="0 0 22 18"><rect x="3" y="1" width="16" height="11" fill="none" stroke="#fff" stroke-width="2"/><rect x="0" y="14" width="22" height="3" fill="#fff"/></svg></div>
  <div class="abs feature-title" style="left:132px">PROGRAMMING LANGUAGES</div>
  <p class="abs feature-text" style="left:132px">Programming Languages that feature the logical operation NAND and other serious inventions.</p>

  <div class="abs feature-icon" style="left:316px"><svg width="20" height="20" viewBox="0 0 20 20"><path d="M7 1h6v7h4l-7 7-7-7h4z" fill="#fff"/><rect x="0" y="15" width="20" height="5" fill="#fff"/></svg></div>
  <div class="abs feature-title" style="left:377px">FREE FOR DOWNLOADING</div>
  <p class="abs feature-text" style="left:377px">Loads of neat Fenestra, Penguix and Orchard utilities free for downloading.</p>

  <div class="abs feature-icon" style="left:574px"><svg width="18" height="18" viewBox="0 0 18 18"><path d="M3 12l9-9 3 3-9 9H3z" fill="#fff"/><path d="M13 2l2-2 3 3-2 2z" fill="#fff"/></svg></div>
  <div class="abs feature-title" style="left:635px">SCRIPTING</div>
  <p class="abs feature-text" style="left:635px">The Serpentix Ministry of silly scripting</p>

  <section class="news">
    <h2 class="abs news-title">LATEST NEWS</h2>
    <p class="abs news-intro">Basically, new is an operator in Corvex to allocate objects. Other than that, the following things are new, too.</p>
    <div class="abs news-photo" style="left:71px;background:linear-gradient(135deg,#3a3a38,#6b6650 60%,#2b2b2b)" role="img" aria-label="Photo of two people working at a laptop in a cafe booth"></div>
    <div class="abs news-photo" style="left:257px;background:linear-gradient(135deg,#e4e4e4,#fafafa 50%,#cfcfcf)" role="img" aria-label="Photo of several white wall clocks"></div>
    <div class="abs news-photo" style="left:442px;background:linear-gradient(135deg,#6f6f6f,#9a9a9a 50%,#555)" role="img" aria-label="Photo of a businessman with a laptop before a chalk-drawn rising bar chart"></div>
    <div class="abs news-photo" style="left:628px;background:linear-gradient(135deg,#1f5c92,#9cc3e3 55%,#2b6aa3)" role="img" aria-label="Photo of a blue keyboard key labelled support"></div>
    <p class="abs news-caption" style="left:71px">Basically, new is an operator in Corvex to allocate objects....</p>
    <p class="abs news-caption" style="left:257px">Basically, new is an operator in Corvex to allocate objects....</p>
    <p class="abs news-caption" style="left:442px">Basically, new is an operator in Corvex to allocate objects....</p>
    <p class="abs news-caption" style="left:628px">Basically, new is an operator in Corvex to allocate objects....</p>
    <span class="abs news-date" style="left:71px">Posted on 11 May 2015</span>
    <span class="abs news-date" style="left:257px">Posted on 11 May 2015</span>
    <span class="abs news-date" style="left:442px">Posted on 11 May 2015</span>
    <span class="abs news-date" style="left:628px">Posted on 11 May 2015</span>
  </section>

  <footer class="site-footer">
    <h3 class="abs footer-head" style="left:88px">Testimonials</h3>
    <span class="abs footer-arrows">&lsaquo;&rsaquo;</span>

    <span class="abs quote-mark" style="left:86px;top:60px">&ldquo;</span>
    <p class="abs quote" style="left:103px">Simply dummy text of the printing and typesetting industry. Lorem Ipsum has been the industry's standard dummy text ever since the 1500s, when an unknown printer took a galley of type and scrambled it to make a type specimen book...</p>
    <span class="abs quote-mark" style="left:284px;top:128px">&rdquo;</span>
    <p class="abs quote-author" style="left:101px"><b>MARLON KEATS</b> Marketing Executive</p>

    <span class="abs quote-mark" style="left:321px;top:60px">&ldquo;</span>
    <p class="abs quote" style="left:338px">Simply dummy text of the printing and typesetting industry. Lorem Ipsum has been the industry's standard dummy text ever since the 1500s, when an unknown printer took a galley of type and scrambled it to make a type specimen book...</p>
    <span class="abs quote-mark" style="left:519px;top:128px">&rdquo;</span>
    <p class="abs quote-author" style="left:337px"><b>MARLON KEATS</b> Marketing Executive</p>

    <h3 class="abs footer-head" style="left:597px">Welcome</h3>
    <ul class="abs footer-links" style="left:597px">
      <li>Home</li><li>Programming</li><li>Languages</li><li>Obfuscation</li><li>Downloads</li><li>Interests</li><li>Contact us</li>
    </ul>
    <h3 class="abs footer-head" style="left:719px">information</h3>
    <ul class="abs footer-links" style="left:719px">
      <li>Privacy Policy</li><li>Terms &amp; Conditions</li><li>Sitemap</li>
    </ul>
  </footer>
  <div class="copyright">&copy; 2015. q-vorx-z. All rights reserved.</div>
</div>
</body>
</html>
```